Marine Services Letterhead design

We need a letterhead design for an Australian owned company in Victoria named K+K Harbour Works Pty Ltd. We provide linesmen and launches to assist the large ships that come into port.
Our colour is orange.
The final design should have a strong nautical theme and communicate safety and reliability.
I would like to use the letter head on invoices so it should print to pdf well.

Target Market(s)

Owners and representatives of shipping companies. It is not for general public

Industry/Entity Type

Nautical

Requirements
Must have
• A shipping theme, not overly complicated, featuring safety orange colours but not all orange of course.
The letterhead should just sit at the top of the page so I can use for invoices.
Nice to have
• Something elegant and stylish
Should not have
• cartoons or pop art

```html
<!DOCTYPE html>
<html lang="en">
<head>
<meta charset="utf-8">
<title>K+K Harbour Works Pty Ltd — Letterhead</title>
<link rel="stylesheet" href="https://fonts.googleapis.com/css2?family=Libre+Baskerville&family=Raleway:wght@400&display=swap">
<style>
  :root {
    --frame-yellow: #f8c50a;
    --paper: #ffffff;
    --ink-dark: #2b2b2b;
    --ink-body: #3a3a3a;
    --mark-tan: #e9b676;
    --mark-ink: #2b2b2b;
  }
  * { margin: 0; padding: 0; box-sizing: border-box; }
  html, body {
    width: 849px;
    height: 1200px;
    overflow: hidden;
    background: var(--paper);
  }
  .letterhead {
    position: relative;
    width: 849px;
    height: 1200px;
    background: var(--paper);
    border: 20px solid var(--frame-yellow);
  }
  .brand-mark {
    position: absolute;
    left: 42px;
    top: 30px;
    width: 130px;
    height: 90px;
    background: var(--mark-tan);
    box-shadow: 2px 3px 5px rgba(0, 0, 0, 0.35);
    display: flex;
    align-items: center;
    justify-content: center;
    text-align: center;
    font-family: "Libre Baskerville", serif;
    font-size: 13px;
    line-height: 1.35;
    color: var(--mark-ink);
    padding: 0 10px;
  }
  .company-details {
    position: absolute;
    left: 196px;
    top: 27px;
  }
  .company-name {
    font-family: "Libre Baskerville", serif;
    font-weight: 400;
    font-size: 19.5px;
    letter-spacing: 0.3px;
    color: var(--ink-dark);
    line-height: 24px;
    margin-bottom: 4px;
  }
  .company-contact {
    font-family: "Raleway", sans-serif;
    font-size: 13.5px;
    line-height: 18px;
    color: var(--ink-body);
    font-style: normal;
  }
</style>
</head>
<body>
  <main class="letterhead">
    <div class="brand-mark">K+K Harbour Works</div>
    <header class="company-details">
      <h1 class="company-name">K+K Harbour Works Pty Ltd</h1>
      <address class="company-contact">
        PO Box 417 Portside 3990<br>
        Phone: 1300 000 418<br>
        ABN: 00123456789
      </address>
    </header>
  </main>
</body>
</html>
```